Powerpoint Presentation

We have a basic 8 page presentation that we would like created on powerpoint. The presentation is very simple dot points and we would like to jazz it up with relevant photos/images relating to the topic on each page.

The topic of the presentation is 'creating a powerful presence and knowing your personal brand' (see attached files).

Target Market(s)

Business women

Requirements
Must have
• Images that match the content on each page

```html
<!DOCTYPE html>
<html lang="en">
<head>
<meta charset="utf-8">
<title>Voice and Language</title>
<link rel="stylesheet" href="https://fonts.googleapis.com/css2?family=Quicksand:wght@400;500&display=swap">
<style>
  :root {
    --brand-orange: #f26a1b;
    --band-orange: #f0650e;
    --title-pink: #ffe3ee;
    --title-glow: #ff2e7e;
    --body-mint: #c8fff0;
    --body-glow: #1fd6b0;
    --caption-ink: #111111;
    --hall-dark: #1a0d0b;
    --hall-mid: #6e2e22;
    --hall-warm: #a24a33;
    --mic-grey: #8d8d8d;
  }
  * { margin: 0; padding: 0; box-sizing: border-box; }
  html, body {
    width: 1200px;
    height: 900px;
    overflow: hidden;
    background: #000;
  }
  .slide {
    position: relative;
    width: 1200px;
    height: 900px;
    overflow: hidden;
    font-family: "Quicksand", sans-serif;
  }
  .slide__backdrop {
    position: absolute;
    inset: 0;
    background:
      radial-gradient(ellipse 170px 200px at 690px 500px, rgba(170,170,170,0.75), rgba(120,120,120,0.35) 60%, transparent 100%),
      radial-gradient(ellipse 700px 380px at 600px 560px, rgba(168,78,54,0.85), transparent 75%),
      linear-gradient(180deg, var(--hall-dark) 0%, #3a1a14 22%, var(--hall-mid) 45%, var(--hall-warm) 70%, #5a2519 100%);
  }
  .brand {
    position: absolute;
    left: 20px;
    top: 22px;
  }
  .brand__mark {
    display: block;
    width: 64px;
    height: 64px;
    background: var(--brand-orange);
    border-radius: 10px;
  }
  .brand__name {
    display: block;
    margin-top: 26px;
    font-size: 31px;
    font-weight: 500;
    color: var(--brand-orange);
    letter-spacing: 0.5px;
  }
  .slide__title {
    position: absolute;
    left: 54px;
    top: 182px;
    font-size: 66px;
    font-weight: 400;
    color: var(--title-pink);
    letter-spacing: 1px;
    text-shadow: 0 0 6px var(--title-glow), 0 0 14px var(--title-glow), 0 0 22px rgba(255,46,126,0.6);
  }
  .point {
    position: absolute;
    left: 56px;
    font-size: 37px;
    font-weight: 400;
    color: var(--body-mint);
    line-height: 1.45;
    text-shadow: 0 0 5px var(--body-glow), 0 0 12px var(--body-glow);
  }
  .point--message { top: 344px; }
  .point--negative { top: 480px; }
  .point__examples { display: block; margin-top: 8px; }
  .credit {
    position: absolute;
    left: 0;
    bottom: 0;
    width: 1200px;
    height: 56px;
    background: var(--band-orange);
    display: flex;
    align-items: center;
    padding-left: 10px;
    font-family: Arial, Helvetica, sans-serif;
    font-size: 16.5px;
    color: var(--caption-ink);
    white-space: nowrap;
  }
</style>
</head>
<body>
  <main class="slide">
    <div class="slide__backdrop" role="img" aria-label="Blurred photo of a seated audience in a hall with a silver stage microphone in sharp focus at the centre"></div>

    <div class="brand">
      <span class="brand__mark"></span>
      <span class="brand__name">open stage talks</span>
    </div>

    <h1 class="slide__title">Voice and Language</h1>

    <p class="point point--message">Get your message across</p>

    <p class="point point--negative">Least amount of<br>negative language<span class="point__examples">(no, never, can’t, don’t)</span></p>

    <footer class="credit">Photo Source: http://brightvoicemind.com/2013/02/26/fearless-public-speaking-for-professionals-developing-your-speaker-identity/</footer>
  </main>
</body>
</html>
```